Web Design Project for selling festive lights

I need a modern and easy to navigate website that is going to sell festive lights.
The name of the site will be "wrenglow" and the logo can be found in the following link: http://qv.zx/Tr8peWm3?
The target group will be people that search for nice decoration lights for their living room, patio and children bedroom.
We need to have a professional look in order to make our webpage distinctive among competition.
The actual products that we are going to sell are cotton ball lights. Pictures can be found in websites like threadandlamp.co.uk and many others.
I need to have a design of the homepage, products pages, customer review page, and shopping cart. The design will be "locked" on a php.

Requirements
Must have
• The fonts used in the design must be compatible with the Greek language because that site will be in Greek.
Nice to have
• Flash and non flash banners

```html
<!DOCTYPE html>
<html lang="en">
<head>
<meta charset="utf-8">
<title>Wrenglow – Cotton Ball Lights</title>
<link href="https://fonts.googleapis.com/css2?family=Arimo:wght@400;700&family=Roboto+Condensed:wght@700;900&family=Caveat&display=swap" rel="stylesheet">
<style>
:root{
  --page:#f1f1f1;
  --bar:#fbfbfb;
  --ink:#333;
  --body:#4a4a4a;
  --muted:#777;
  --line:#d3d3d3;
  --dark:#1c1c1c;
  --dark2:#3a3a3a;
  --yellow:#f8c41c;
  --orange:#e8560f;
  --social:#6a6a6a;
  --panel:#ececec;
}
*{box-sizing:border-box;margin:0;padding:0}
html,body{width:1200px;height:1196px;overflow:hidden}
body{position:relative;background:var(--page);font-family:Arimo,Arial,sans-serif;color:var(--ink)}
.abs{position:absolute}

.topbar{left:0;top:0;width:1200px;height:46px;background:var(--bar);border-bottom:1px solid #e0e0e0}
.logo{left:108px;top:12px;width:190px;height:116px;background:#dcdcdc;border:1px solid #c8c8c8;box-shadow:0 2px 4px rgba(0,0,0,.15)}
.logo-inner{position:absolute;left:14px;top:2px;width:160px;height:96px;background:#fff;border-radius:50%;display:flex;align-items:center;justify-content:center;gap:6px}
.logo-dot{width:12px;height:12px;border-radius:50%;background:var(--yellow)}
.logo-name{font-family:Arimo,Arial,sans-serif;font-size:21px;font-weight:700;color:#333}
.phone{left:318px;top:11px;font-family:"Roboto Condensed",Arial,sans-serif;font-weight:700;font-size:22px;color:#3a3a3a}
.topnav{left:530px;top:16px;display:flex;font-size:13px;color:#333}
.topnav span{padding:0 8px;border-left:1px solid #ddd;line-height:15px}
.topnav span:first-child{border-left:none}
.cart{left:1015px;top:12px;display:flex;align-items:center;gap:6px;font-size:13px;color:#444}
.follow{left:720px;top:82px;font-family:Caveat,cursive;font-size:30px;color:#666}
.social{top:72px;width:64px;height:64px;border-radius:50%;background:var(--social);display:flex;align-items:center;justify-content:center}

.mainnav{left:110px;top:165px;width:980px;height:46px;border-radius:5px 5px 0 0;background:linear-gradient(#3b3b3b,#0d0d0d);display:flex;color:#fff;font-size:15px}
.mainnav .item{padding:0 16px;line-height:46px;border-right:1px solid #2a2a2a;box-shadow:1px 0 0 #444}
.mainnav .home{width:54px;padding:0;display:flex;align-items:center;justify-content:center}
.mainnav .active{background:var(--yellow);color:#222;padding:0 17px 0 15px}

.banner{left:110px;top:211px;width:981px;height:344px;background:linear-gradient(90deg,#6a2a44 0%,#3e1848 50%,#1e1e58 100%);box-shadow:0 12px 24px rgba(0,0,0,.25)}
.banner-text{color:#fff;font-family:"Roboto Condensed",Arial,sans-serif;font-weight:900;text-shadow:0 2px 3px rgba(0,0,0,.5);white-space:nowrap}
.b-welcome{left:147px;top:278px;font-size:32px}
.b-name{left:246px;top:318px;font-size:62px}
.b-line1{left:187px;top:441px;font-size:24px;font-weight:700;word-spacing:7px}
.b-line2{left:187px;top:475px;font-size:24px;font-weight:700;word-spacing:5px}
.b-line2 b{font-size:40px;font-weight:900}
.arrow{top:345px;width:54px;height:54px;border-radius:50%;background:linear-gradient(#fff,#dcdcdc);box-shadow:0 2px 5px rgba(0,0,0,.35);display:flex;align-items:center;justify-content:center}
.dots{left:585px;top:560px;display:flex;gap:4px}
.dots i{width:12px;height:12px;border-radius:50%;background:#3a3a3a}
.dots i:first-child{background:var(--orange)}

.card{top:593px;width:322px;height:204px;background:var(--panel);border:2px solid #d6d6d6;border-radius:10px;box-shadow:0 10px 12px -8px rgba(0,0,0,.25)}
.ribbon{top:607px;height:28px;background:linear-gradient(90deg,#111,#3a3a3a);color:#fff;font-size:14.5px;line-height:28px;padding-left:21px}
.fold{top:635px;width:0;height:0;border-top:10px solid #000}
.thumb{width:92px;height:62px;border:2px solid #fff;outline:1px solid #ccc;background:radial-gradient(circle at 50% 45%,#e8c690 0%,#6a5a48 40%,#111 75%)}
.combo-photo{left:450px;top:648px;width:294px;height:128px;border:2px solid #fff;outline:1px solid #ccc;background:#fff}
.made-photo{left:779px;top:650px;width:122px;height:98px;border:2px solid #fff;outline:1px solid #ccc;background:linear-gradient(135deg,#c98a5a,#e8a070 40%,#a8b8c8 70%,#d0c0c8)}
.made-text{left:912px;top:646px;width:152px;font-size:14.5px;line-height:23px;color:#222}
.readmore{left:781px;top:771px;font-size:12px;color:#222;text-decoration:underline}

.welcome{left:110px;top:835px;width:980px;height:242px;background:#f6f6f6;border:2px solid #d6d6d6;border-radius:10px;box-shadow:0 10px 12px -8px rgba(0,0,0,.25)}
.welcome-head{left:99px;top:851px;width:991px;height:38px;background:linear-gradient(90deg,#111,#333 60%,#222);color:#fff;font-size:17px;font-weight:700;line-height:38px;padding-left:21px}
.welcome-body{left:127px;top:900px;width:948px;font-size:13.4px;line-height:23px;color:var(--body)}
.welcome-body p+p{margin-top:23px}
.welcome-body span{display:block;white-space:nowrap}

.footer{left:0;top:1138px;width:1200px;height:58px;background:#f4f4f4;border-top:1px solid #dcdcdc}
.copy{left:114px;top:1160px;font-size:14px;color:#333}
.legal{left:440px;top:1162px;font-size:12.5px;color:#444}
.accept{left:875px;top:1162px;font-size:12px;color:#444}
.pay{top:1160px;width:24px;height:16px;border-radius:2px}
</style>
</head>
<body>

<div class="abs topbar"></div>
<div class="abs logo"><div class="logo-inner"><span class="logo-dot"></span><span class="logo-name">Wrenglow</span></div></div>
<div class="abs phone">01632 960 418</div>
<nav class="abs topnav"><span>Buy</span><span>About</span><span>Contact</span><span>Commercial</span><span>Gallery</span><span>Blog</span><span>Help</span><span>Account</span></nav>
<div class="abs cart">
  <svg width="24" height="22" viewBox="0 0 24 22"><path d="M1 2h4l3 12h12l2-8H7" fill="none" stroke="#777" stroke-width="1.8"/><circle cx="10" cy="18" r="2" fill="#777"/><circle cx="18" cy="18" r="2" fill="#777"/></svg>
  <span>Cart (0)</span>
</div>

<div class="abs follow">Follow us on</div>
<svg class="abs" style="left:820px;top:118px" width="62" height="18" viewBox="0 0 62 18"><path d="M2 8c16 10 36 10 56 2" fill="none" stroke="#777" stroke-width="1.5"/><path d="M52 6l7 4-7 4" fill="none" stroke="#777" stroke-width="1.5"/></svg>
<div class="abs social" style="left:883px" aria-label="Social profile"></div>
<div class="abs social" style="left:954px" aria-label="Social profile"></div>
<div class="abs social" style="left:1025px" aria-label="Email">
  <svg width="36" height="24" viewBox="0 0 36 24"><rect x="1" y="1" width="34" height="22" fill="#fff"/><path d="M1 1l17 12L35 1" fill="none" stroke="#6a6a6a" stroke-width="2"/></svg>
</div>

<nav class="abs mainnav">
  <div class="item home"><svg width="22" height="20" viewBox="0 0 22 20"><path d="M11 1L1 10h3v9h5v-6h4v6h5v-9h3z" fill="#fff"/></svg></div>
  <div class="item active">Pre-selected</div>
  <div class="item">Pick your own</div>
  <div class="item">Big Lamps</div>
  <div class="item">Gift Vouchers</div>
  <div class="item">Replacements</div>
</nav>

<div class="abs banner" role="img" aria-label="Banner photograph of colourful festive light effects"></div>
<div class="abs banner-text b-welcome">Welcome to</div>
<div class="abs banner-text b-name">Wrenglow</div>
<div class="abs banner-text b-line1">Lorem ipsum dolor sit amet, consectetur adipisicing elit, sed do eiusmod</div>
<div class="abs banner-text b-line2"><b>tempor</b> incididunt ut labore et dolore <b>magna</b> aliqua.</div>
<div class="abs arrow" style="left:81px"><svg width="20" height="22" viewBox="0 0 20 22"><path d="M9 2L3 11l6 9M17 2l-6 9 6 9" fill="none" stroke="#777" stroke-width="3"/></svg></div>
<div class="abs arrow" style="left:1062px"><svg width="20" height="22" viewBox="0 0 20 22"><path d="M3 2l6 9-6 9M11 2l6 9-6 9" fill="none" stroke="#777" stroke-width="3"/></svg></div>
<div class="abs dots"><i></i><i></i><i></i><i></i></div>

<div class="abs card" style="left:110px"></div>
<div class="abs card" style="left:438px"></div>
<div class="abs card" style="left:766px"></div>

<div class="abs ribbon" style="left:99px;width:333px">Some choice combinations...</div>
<div class="abs fold" style="left:99px;border-left:11px solid transparent"></div>
<div class="abs ribbon" style="left:437px;width:324px;padding-left:11px">Create your own...</div>
<div class="abs ribbon" style="left:766px;width:334px;padding-left:10px">See how our lamps are made</div>
<div class="abs fold" style="left:1089px;border-right:11px solid transparent"></div>

<div class="abs thumb" style="left:124px;top:650px" role="img" aria-label="Cotton ball light string glowing"></div>
<div class="abs thumb" style="left:225px;top:650px" role="img" aria-label="Cotton ball light string glowing"></div>
<div class="abs thumb" style="left:326px;top:650px" role="img" aria-label="Cotton ball light string glowing"></div>
<div class="abs thumb" style="left:124px;top:721px" role="img" aria-label="Cotton ball light string glowing"></div>
<div class="abs thumb" style="left:225px;top:721px" role="img" aria-label="Cotton ball light string glowing"></div>
<div class="abs thumb" style="left:326px;top:721px" role="img" aria-label="Cotton ball light string glowing"></div>

<div class="abs combo-photo" role="img" aria-label="Coloured cotton balls hanging on a white cable"></div>

<div class="abs made-photo" role="img" aria-label="Lamps being made by hand outdoors"></div>
<div class="abs made-text">Our Lamps are hand made in the fresh air<br>– see the process!</div>
<div class="abs readmore">readmore →</div>

<div class="abs welcome"></div>
<div class="abs welcome-head">Welcome to Wrenglow</div>
<div class="abs fold" style="left:99px;top:889px;border-left:11px solid transparent"></div>
<div class="abs welcome-body">
  <p><span>Lorem ipsum dolor sit amet, consectetur adipisicing elit, sed do eiusmod tempor incididunt ut labore et dolore magna aliqua. Ut enim ad minim veniam,</span><span>quis nostrud exercitation ullamco laboris nisi ut aliquip ex ea commodo consequat. Duis aute irure dolor in reprehenderit in voluptate velit esse cillum dolore</span><span>eu fugiat nulla pariatur. Excepteur sint occaecat cupidatat non proident, sunt in culpa qui officia deserunt mollit anim id est laborum.</span></p>
  <p><span>Lorem ipsum dolor sit amet, consectetur adipisicing elit, sed do eiusmod tempor incididunt ut labore et dolore magna aliqua. Ut enim ad minim veniam,</span><span>quis nostrud exercitation ullamco laboris nisi ut aliquip ex ea commodo consequat. Duis aute irure dolor in reprehenderit in voluptate velit esse cillum dolore</span><span>eu fugiat nulla pariatur. Excepteur sint occaecat cupidatat non proident, sunt in culpa qui officia deserunt mollit anim id est laborum.</span></p>
</div>

<footer class="abs footer"></footer>
<div class="abs copy">Copyright © 2012 Wrenglow, All Rights Reserved!</div>
<div class="abs legal">::&nbsp; Terms &amp; Conditions | Privacy Policy</div>
<div class="abs accept">We accept :</div>
<div class="abs pay" style="left:945px;background:#d8d8d8"></div>
<div class="abs pay" style="left:974px;background:#6f8fc8"></div>
<div class="abs pay" style="left:1003px;background:#3a52a8"></div>
<div class="abs pay" style="left:1032px;background:#a858a8"></div>
<div class="abs pay" style="left:1061px;background:#3b78c8"></div>

</body>
</html>
```